Fundraising Study Day East of England. Lift the January blues!

A flyer to advertise a fundraising event of lectures for dental hygienists and therapists in support of the exemption campaign. Currently dental hygienists and therapists require a prescription to deliver certain treatment or recommend certain toothpastes. If we are successful in the campaign we will be able to treat patients without these restrictions.

Industry/Entity Type

Dental

```html
<!DOCTYPE html>
<html lang="en">
<head>
<meta charset="utf-8">
<title>Lift the January Blues – Fundraising Study Day</title>
<link rel="stylesheet" href="https://fonts.googleapis.com/css2?family=Anton&family=Lato:wght@400;700&display=swap">
<style>
  :root {
    --brand-blue: #0c9cc4;
    --panel-blue: #0aa3c9;
    --wave-blue: #4cc4de;
    --wave-light: #93d9ea;
    --bar-blue: #4ec3df;
    --body-grey: #6a6a6a;
    --white: #ffffff;
  }
  * { margin: 0; padding: 0; box-sizing: border-box; }
  html, body { width: 990px; height: 1200px; overflow: hidden; background: var(--white); }
  .flyer { position: relative; width: 990px; height: 1200px; overflow: hidden; background: var(--white); font-family: "Lato", sans-serif; }
  .backdrop { position: absolute; inset: 0; }
  .panel-photo { position: absolute; left: 640px; top: 300px; width: 350px; height: 560px;
    background: radial-gradient(ellipse at 55% 45%, rgba(255,255,255,0.16), rgba(255,255,255,0) 70%); }

  .eyebrow { position: absolute; left: 42px; top: 36px; font-size: 19px; color: var(--brand-blue); letter-spacing: 0.2px; }
  .headline { position: absolute; left: 40px; top: 66px; font-family: "Anton", sans-serif; font-size: 88px; line-height: 96px; color: var(--brand-blue); letter-spacing: -2px; text-transform: uppercase; }
  .event-date, .event-venue { position: absolute; left: 42px; font-size: 25px; color: var(--brand-blue); }
  .event-date { top: 280px; }
  .event-venue { top: 318px; font-size: 24px; }

  .slot-bar { position: absolute; left: 0; width: 228px; height: 36px; background: var(--bar-blue);
    clip-path: polygon(0 0, 88% 0, 100% 100%, 0 100%); font-family: "Anton", sans-serif; font-size: 27px; line-height: 36px; color: var(--white); padding-left: 42px; letter-spacing: -0.5px; }
  .slot-text { position: absolute; left: 42px; width: 530px; font-size: 17.5px; line-height: 24px; color: var(--body-grey); }

  .tooth-badge { position: absolute; left: 752px; top: 42px; width: 172px; height: 172px; }
  .intro { position: absolute; left: 680px; width: 300px; text-align: center; color: var(--white); font-size: 20px; line-height: 25.5px; }
  .book-now { position: absolute; left: 688px; top: 720px; width: 261px; height: 47px; border: 2px solid var(--white);
    font-family: "Anton", sans-serif; color: var(--white); font-size: 27px; line-height: 43px; text-align: center; letter-spacing: 0.5px; }
  .booking-link { position: absolute; left: 680px; top: 800px; width: 282px; text-align: center; color: var(--white); font-size: 19.5px; line-height: 25.5px; word-break: break-all; }
  .price-badge { position: absolute; left: 705px; top: 943px; width: 216px; height: 216px; border-radius: 50%; background: var(--white);
    box-shadow: 0 3px 8px rgba(0,0,0,0.2); }
  .price-inner { position: absolute; inset: 9px; border-radius: 50%; background: radial-gradient(circle at 45% 35%, #ffffff, #e7ebee 70%, #d8dde1);
    text-align: center; font-family: "Anton", sans-serif; color: var(--brand-blue); }
  .price-label { display: block; margin-top: 32px; font-size: 30px; line-height: 34px; }
  .price-value { display: block; font-size: 64px; line-height: 70px; letter-spacing: -2px; }
</style>
</head>
<body>
<main class="flyer">
  <svg class="backdrop" width="990" height="1200" viewBox="0 0 990 1200" aria-hidden="true">
    <path d="M555,0 C690,200 705,450 645,700 C595,900 545,1050 528,1200 L990,1200 L990,0 Z" fill="var(--wave-blue)"/>
    <path d="M612,0 C720,210 725,470 672,710 C622,915 575,1060 560,1200" fill="none" stroke="var(--wave-light)" stroke-width="9"/>
    <path d="M645,0 C745,220 745,480 695,720 C645,920 598,1062 585,1200 L990,1200 L990,0 Z" fill="var(--panel-blue)"/>
  </svg>
  <div class="panel-photo" role="img" aria-label="Faint photograph of a smiling dental professional blended into the blue panel"></div>

  <p class="eyebrow">FUNDRAISING STUDY DAY EAST OF ENGLAND.</p>
  <h1 class="headline">Lift the<br>January Blues!</h1>
  <p class="event-date">Fri 19 January 2018, 09:00 – 16:30 GMT</p>
  <p class="event-venue">Larchmont Hotel, Meteor Road Hatfield AL10 4QX</p>

  <div class="slot-bar" style="top:373px">9.30 - 10.15</div>
  <p class="slot-text" style="top:425px">Helen Marsh: Immediate past president of the AHTS will be updating us on all things ECPD</p>

  <div class="slot-bar" style="top:484px">10.15 - 11.00</div>
  <p class="slot-text" style="top:536px">Megan Ashdown: Will provide an update on teeth whiteing and explain how social media has impacted her business Clara Winslow: Our internationally acclaimed speaker will update our knowledge of periodontal disease and nutrition and new technologies</p>
  <p class="slot-text" style="top:656px">11.00 - 11.30&nbsp; Break</p>

  <div class="slot-bar" style="top:684px">11.30 - 13.00</div>
  <p class="slot-text" style="top:738px">Orla Bennett &amp; Laura Pryce: Will be providing a combined presentation on 'Scaling your business' and start to finish Ultrasonic techniques. The aim being to build our business with effective communications, systems and protocols. This sessions promises audience participation!</p>
  <p class="slot-text" style="top:883px">12 - 14.00 lunch</p>

  <div class="slot-bar" style="top:915px">14 - 15.00</div>
  <p class="slot-text" style="top:970px">Sam Khatri: Save your back. All things posture.</p>
  <p class="slot-text" style="top:1004px">15.00 - 15.30 Break</p>

  <div class="slot-bar" style="top:1039px">15.30 16.30</div>
  <p class="slot-text" style="top:1094px; width:470px">Clara Winslow: Our internationally acclaimed speaker will update our knowledge of periodontal disease and nutrition and new technologies.</p>

  <svg class="tooth-badge" viewBox="0 0 172 172" role="img" aria-label="Tooth icon">
    <circle cx="86" cy="86" r="83" fill="none" stroke="var(--white)" stroke-width="3"/>
    <path d="M60,50 C72,44 80,50 86,53 C92,50 100,44 112,50 C124,57 122,78 116,92 C112,102 112,118 106,128 C101,135 97,128 95,118 C93,108 91,102 86,102 C81,102 79,108 77,118 C75,128 71,135 66,128 C60,118 60,102 56,92 C50,78 48,57 60,50 Z" fill="none" stroke="var(--white)" stroke-width="4" stroke-linejoin="round"/>
  </svg>

  <p class="intro" style="top:242px">A fundraising event to support our exemptions project. The day will consist of a series of presentations ranging from the new ECPD to new technologies.</p>
  <p class="intro" style="top:420px">The aim, being to enhance our learning and raise funds to support the exemptions campaign.</p>
  <p class="intro" style="top:547px">The speaker line includes some of the UK and Irelands most respected dental professionals in our field.</p>

  <div class="book-now">BOOK NOW</div>
  <p class="booking-link">https://www.ticketfolio.co.uk/e/fundraising-study-day-east-of-england-lift-the-january-blues-tickets-48213907</p>

  <div class="price-badge">
    <div class="price-inner">
      <span class="price-label">COST</span>
      <span class="price-value">£101.48</span>
    </div>
  </div>
</main>
</body>
</html>
```